SilverLedgerOak - Double Sided Business Card

We are looking for design options or our business cards. We are a Business Solutions and HR solutions Provider - the theme is business, for this card.

Our brand colours are represented within our logo.

Details needed to be put on the front of the business card are:

Employees name: [Sample Name]
Role: [Sample Role]

Address: Suite 4 - Level 3/48 Halloran Avenue Parramatta NSW 2150
M: 0000 000 000
P: 1300 847 213
F: 1300 847 286
E: sample@silverledgeroak.com.au
www.silverledgeroak.com.au
Updates

Reason: Hello, could we please increase our deadline by 5 days. Thanking you, Tess

Target Market(s)

Business Owners, also Candidates looking for Employment

Industry/Entity Type

Business

Contact Information for Business Card

Role: [Sample Role]

M: 0000 000 000
P: 1300 847 213
F: 1300 847 286

Font styles to use
Sans Serif

Colors
3276b5
3176b5
0455a3
85abd2
cfdeed
ffffff
000000
1b1b1b
757575

Requirements
Must have
• Details needed to be put on the front of the business card are:
• Employees name: [Sample Name]
• Role: [Sample Role]
• Address: Suite 4 - Level 3/48 Halloran Avenue Parramatta NSW 2150
• M: 0000 000 000
• P: 1300 847 213
• F: 1300 847 286
• E: sample@silverledgeroak.com.au
• www.silverledgeroak.com.au
Nice to have
• Simplicity, clean and professional.

```html
<!DOCTYPE html>
<html lang="en">
<head>
<meta charset="utf-8">
<title>SilverLedgerOak – Business Card</title>
<link href="https://fonts.googleapis.com/css2?family=Open+Sans:wght@400;600;700&display=swap" rel="stylesheet">
<style>
  :root {
    --blue: #0455a3;
    --blue-mid: #3276b5;
    --blue-soft: #85abd2;
    --blue-pale: #cfdeed;
    --navy: #0b1c36;
    --white: #ffffff;
    --ink: #1b1b1b;
    --grey: #757575;
    --stage: #1b1b1b;
  }
  * { margin: 0; padding: 0; box-sizing: border-box; }
  html, body {
    width: 1200px; height: 900px; overflow: hidden;
    background: var(--stage);
    font-family: "Open Sans", Arial, sans-serif;
  }
  .sheet {
    width: 1200px; height: 900px;
    display: flex; flex-direction: column; align-items: center; justify-content: center;
    gap: 50px;
  }
  .card {
    position: relative; width: 600px; height: 343px; overflow: hidden;
    box-shadow: 0 10px 30px rgba(0,0,0,.5);
  }
  .card svg.shapes { position: absolute; inset: 0; }

  /* front */
  .card-front { background: var(--white); }
  .brand {
    position: absolute; left: 318px; top: 34px; width: 262px;
    display: flex; flex-direction: column; align-items: center;
  }
  .brand-row { display: flex; align-items: center; gap: 10px; }
  .brand-square { width: 22px; height: 22px; background: var(--blue); }
  .brand-name { font-weight: 700; font-size: 26px; color: var(--navy); letter-spacing: .3px; }
  .brand-tagline {
    margin-top: 8px; padding-top: 4px; border-top: 1px solid var(--ink);
    font-size: 8.5px; font-weight: 700; color: var(--ink); white-space: nowrap;
  }
  .social { position: absolute; left: 425px; top: 178px; display: flex; gap: 8px; }
  .social span { width: 17px; height: 17px; border: 1.4px solid var(--white); border-radius: 50%; }

  .person { position: absolute; left: 30px; top: 122px; color: var(--white); line-height: 16px; }
  .person-name { font-weight: 700; font-size: 14px; letter-spacing: .3px; }
  .person-role { font-size: 12px; color: var(--blue-pale); }

  .address {
    position: absolute; left: 30px; top: 166px; color: var(--white);
    font-style: normal; font-size: 11.5px; line-height: 15px;
  }
  .address strong { font-weight: 700; font-size: 12px; }

  .contacts { position: absolute; left: 30px; top: 218px; list-style: none; color: var(--white); font-size: 11.5px; }
  .contacts li { display: flex; align-items: center; gap: 8px; height: 15px; }
  .contacts svg { width: 12px; height: 12px; flex: none; }

  .web-front {
    position: absolute; left: 30px; top: 300px; color: var(--white);
    font-size: 16px; letter-spacing: 2px;
  }

  /* back */
  .card-back { background: linear-gradient(135deg, #0a4f9c 0%, #0a3d7a 45%, #071f42 100%); }
  .back-brand {
    position: absolute; left: 0; right: 0; top: 130px;
    display: flex; justify-content: center; align-items: center; gap: 12px;
  }
  .back-brand .brand-square { background: var(--white); width: 26px; height: 26px; }
  .back-brand .brand-name { color: var(--white); font-size: 30px; }
  .back-web {
    position: absolute; left: 0; right: 0; top: 262px;
    display: flex; justify-content: center; align-items: center; gap: 14px;
    color: var(--white); font-size: 14px; letter-spacing: 2.5px;
  }
  .back-web i { display: block; width: 90px; height: 1px; background: var(--blue-pale); }
</style>
</head>
<body>
<main class="sheet">

  <section class="card card-front" aria-label="Business card front">
    <svg class="shapes" viewBox="0 0 600 343" aria-hidden="true">
      <polygon points="0,118 205,118 262,152 600,152 600,245 330,245 330,343 0,343" fill="var(--blue)"/>
      <polygon points="205,118 222,118 279,152 262,152" fill="#e4e8ee"/>
      <polygon points="0,160 262,160 305,200 305,284 0,284" fill="var(--navy)"/>
      <polygon points="262,160 285,160 330,200 305,200" fill="#d9dee6"/>
      <rect x="0" y="284" width="330" height="4" fill="var(--blue-soft)"/>
      <rect x="330" y="245" width="270" height="98" fill="#f2f4f7"/>
    </svg>

    <div class="brand">
      <div class="brand-row">
        <span class="brand-square"></span>
        <span class="brand-name">SilverLedgerOak</span>
      </div>
      <div class="brand-tagline">Guiding small to mid-size firms toward their full potential</div>
    </div>

    <div class="social" aria-label="Social links"><span></span><span></span><span></span><span></span></div>

    <div class="person">
      <p class="person-name">MARK DELANEY</p>
      <p class="person-role">Director</p>
    </div>

    <address class="address">
      <strong>SilverLedgerOak</strong><br>
      Suite 4 - Level 3/48 Halloran Avenue<br>
      Kellmore NSW 2741
    </address>

    <ul class="contacts">
      <li><svg viewBox="0 0 12 12"><circle cx="6" cy="6" r="6" fill="var(--blue-mid)"/><rect x="4" y="2.5" width="4" height="7" rx=".8" fill="none" stroke="#fff" stroke-width="1"/></svg>0412 306 758</li>
      <li><svg viewBox="0 0 12 12"><circle cx="6" cy="6" r="6" fill="var(--blue-mid)"/><path d="M4 3 L5.2 4.4 L4.6 5.2 Q5.5 6.8 6.8 7.4 L7.6 6.8 L9 8 L8.2 9 Q5 8.5 3.2 4 Z" fill="#fff"/></svg>1300 847 213</li>
      <li><svg viewBox="0 0 12 12"><circle cx="6" cy="6" r="6" fill="var(--blue-mid)"/><rect x="3" y="5" width="6" height="3.5" fill="#fff"/><rect x="4" y="2.8" width="4" height="2" fill="#fff"/></svg>1300 847 286</li>
      <li><svg viewBox="0 0 12 12"><circle cx="6" cy="6" r="6" fill="var(--blue-mid)"/><rect x="3" y="4" width="6" height="4" fill="#fff"/><path d="M3 4 L6 6.3 L9 4" fill="none" stroke="var(--blue-mid)" stroke-width=".8"/></svg>sample@silverledgeroak.com.au</li>
    </ul>

    <p class="web-front">www.silverledgeroak.com.au</p>
  </section>

  <section class="card card-back" aria-label="Business card back">
    <svg class="shapes" viewBox="0 0 600 343" aria-hidden="true">
      <polygon points="60,343 250,100 330,100 140,343" fill="rgba(255,255,255,.04)"/>
      <polygon points="230,343 420,60 480,60 290,343" fill="rgba(255,255,255,.035)"/>
      <polygon points="0,343 0,200 120,40 170,40" fill="rgba(0,0,0,.08)"/>
    </svg>
    <div class="back-brand">
      <span class="brand-square"></span>
      <span class="brand-name">SilverLedgerOak</span>
    </div>
    <div class="back-web"><i></i><span>www.silverledgeroak.com.au</span><i></i></div>
  </section>

</main>
</body>
</html>
```